fizzy drinks label design

I want to design fizzy drink label for 3 flavors : black grapes, red apple and mojito, band name kestrola, product name KOLTA , product will be in plastic bottle, label size 198 mm X 66mm

```html
<!DOCTYPE html>
<html lang="en">
<head>
<meta charset="utf-8">
<title>KOLTA Fizzy Drink Labels</title>
<link rel="stylesheet" href="https://fonts.googleapis.com/css2?family=Open+Sans:ital,wght@0,400;0,700;0,800;1,400&family=Manrope:wght@400;500&family=Yellowtail&display=swap">
<style>
  :root {
    --stage: #272830;
    --white: #ffffff;
    --gold: #d9a94a;
    --gold-light: #f3d98b;
    --grape-deep: #2e0638;
    --grape-mid: #5a1670;
    --grape-glow: #d472c8;
    --apple-deep: #7c0308;
    --apple-mid: #c0151a;
    --apple-glow: #ffb08a;
    --lime-deep: #bfdd8a;
    --lime-mid: #d6eab0;
    --lime-glow: #ffffff;
    --lime-ink: #1e2a14;
    --lime-name: #157a3a;
    --kolta-gold: #e8c35e;
  }
  * { box-sizing: border-box; margin: 0; padding: 0; }
  html, body { width: 1200px; height: 1000px; overflow: hidden; background: var(--stage); }
  .canvas { position: relative; width: 1200px; height: 1000px; font-family: "Open Sans", sans-serif; }

  .size-note {
    position: absolute; left: 321px; top: 143px;
    font-family: "Manrope", sans-serif; font-size: 14px; color: var(--white);
  }

  .label {
    position: absolute; left: 319px; width: 561px; height: 187px; overflow: hidden;
    border-bottom: 4px solid var(--gold);
  }
  .label::after {
    content: ""; position: absolute; left: 0; right: 0; bottom: -4px; height: 4px;
    background: linear-gradient(90deg, #a87a2a, var(--gold-light) 50%, #a87a2a);
  }
  .label--grape { top: 167px; color: var(--white);
    background: radial-gradient(ellipse 150px 120px at 280px 95px, var(--grape-glow), var(--grape-mid) 70%, var(--grape-deep) 100%), var(--grape-deep); }
  .label--apple { top: 396px; color: var(--white);
    background: radial-gradient(ellipse 150px 120px at 280px 95px, var(--apple-glow), var(--apple-mid) 70%, var(--apple-deep) 100%), var(--apple-deep); }
  .label--lime { top: 622px; color: var(--lime-ink);
    background: radial-gradient(ellipse 150px 120px at 280px 95px, var(--lime-glow), var(--lime-mid) 70%, var(--lime-deep) 100%), var(--lime-deep); }

  .copy { position: absolute; top: 14px; width: 130px; font-size: 6.1px; line-height: 7.9px; font-style: italic; }
  .copy--left { left: 16px; }
  .copy--right { left: 415px; top: 17px; }
  .copy h3 { font-style: normal; font-weight: 700; font-size: 6.6px; line-height: 9px; }
  .copy p + p { margin-top: 7.9px; }

  .brand-name {
    position: absolute; left: 258px; top: 16px;
    font-weight: 700; font-size: 11px; color: var(--white);
    display: flex; align-items: center; gap: 3px;
  }
  .label--lime .brand-name { color: var(--lime-ink); }
  .brand-dot { width: 5px; height: 5px; border-radius: 50%; background: currentColor; }

  .fruit-art {
    position: absolute; left: 186px; top: 44px; width: 186px; height: 138px; border-radius: 50%;
  }
  .label--grape .fruit-art { background: radial-gradient(ellipse at 45% 50%, #2a2840 0 35%, #5c8a3e 55%, rgba(180,200,230,0.35) 75%, transparent 78%); }
  .label--apple .fruit-art { background: radial-gradient(ellipse at 50% 45%, #b3101a 0 38%, #f3d6c8 55%, rgba(200,220,235,0.35) 75%, transparent 78%); }
  .label--lime .fruit-art { background: radial-gradient(ellipse at 50% 50%, #8cc63f 0 40%, #4e8f2e 55%, rgba(160,200,230,0.35) 75%, transparent 78%); }

  .product-name {
    position: absolute; left: 162px; top: 66px; transform: rotate(-38deg); transform-origin: left top;
    font-weight: 800; font-size: 30px; letter-spacing: 1px; color: var(--kolta-gold);
  }
  .flavor-name {
    position: absolute; top: 150px; font-family: "Yellowtail", cursive; font-size: 18px; color: var(--white);
  }
  .label--grape .flavor-name { left: 306px; }
  .label--apple .flavor-name { left: 304px; }
  .label--lime .flavor-name { left: 305px; color: var(--lime-name); }

  .caption {
    position: absolute; left: 0; width: 1200px; top: 855px; text-align: center;
    font-family: "Manrope", sans-serif; font-size: 14px; line-height: 17px; color: var(--white);
  }
</style>
</head>
<body>
<div class="canvas">
  <div class="size-note">198x66 mm</div>

  <section class="label label--grape">
    <div class="copy copy--left">
      <h3>INGREDIENTS</h3>
      <p>Lorem ipsum dolor sit amet, consectetuer adipiscing elit, sed diam nonummy nibh euismod tincidunt ut laoreet dolore magna aliquam erat volutpat. Ut wisi enim ad minim veniam, quis nostrud exea commodo consequat. Duis</p>
      <p>Lorem ipsum dolor sit amet, consectetuer adipiscing elit, sed diam nonummy nibh euismod tincidunt ut laoreet dolore magna aliquam erat volutpat. Ut wisi enim ad minim</p>
      <p>Lorem ipsum dolor sit amet, consectetuer adipiscing elit, sed diam nonummy nibh euismod tincidunt ut laoreet dolore magna aliquam erat volutpat. Ut wisi enim ad minim veniam, quis nostrud exea commodo consequat. Duis</p>
    </div>
    <div class="fruit-art" role="img" aria-label="Bunch of black grapes with vine leaves inside a splash of water"></div>
    <div class="brand-name"><span class="brand-dot"></span>kestrola</div>
    <div class="product-name">KOLTA</div>
    <div class="flavor-name">Black Grapes</div>
    <div class="copy copy--right">
      <p>Lorem ipsum dolor sit amet, consectetuer adipiscing elit, sed diam nonummy nibh euismod tincidunt ut laoreet dolore magna aliquam erat volutpat. Ut wisi enim ad minim veniam, quis nostrud exea commodo consequat. Duis</p>
      <p>Lorem ipsum dolor sit amet, consectetuer adipiscing elit, sed diam nonummy nibh euismod tincidunt ut laoreet dolore magna aliquam erat volutpat. Ut wisi enim ad minim veniam, quis nostrud exea commodo consequat. Duis</p>
      <p>Lorem ipsum dolor sit amet, consectetuer adipiscing elit, sed diam nonummy nibh euismod tincidunt ut laoreet dolore magna aliquam erat volutpat. Ut wisi enim ad minim veniam, quis nostrud exea commodo consequat. Duis</p>
    </div>
  </section>

  <section class="label label--apple">
    <div class="copy copy--left">
      <h3>INGREDIENTS</h3>
      <p>Lorem ipsum dolor sit amet, consectetuer adipiscing elit, sed diam nonummy nibh euismod tincidunt ut laoreet dolore magna aliquam erat volutpat. Ut wisi enim ad minim veniam, quis nostrud exea commodo consequat. Duis</p>
      <p>Lorem ipsum dolor sit amet, consectetuer adipiscing elit, sed diam nonummy nibh euismod tincidunt ut laoreet dolore magna aliquam erat volutpat. Ut wisi enim ad minim</p>
      <p>Lorem ipsum dolor sit amet, consectetuer adipiscing elit, sed diam nonummy nibh euismod tincidunt ut laoreet dolore magna aliquam erat volutpat. Ut wisi enim ad minim veniam, quis nostrud exea commodo consequat. Duis</p>
    </div>
    <div class="fruit-art" role="img" aria-label="Two red apples and a cut apple half inside a splash of water"></div>
    <div class="brand-name"><span class="brand-dot"></span>kestrola</div>
    <div class="product-name">KOLTA</div>
    <div class="flavor-name">Red Apple</div>
    <div class="copy copy--right">
      <p>Lorem ipsum dolor sit amet, consectetuer adipiscing elit, sed diam nonummy nibh euismod tincidunt ut laoreet dolore magna aliquam erat volutpat. Ut wisi enim ad minim veniam, quis nostrud exea commodo consequat. Duis</p>
      <p>Lorem ipsum dolor sit amet, consectetuer adipiscing elit, sed diam nonummy nibh euismod tincidunt ut laoreet dolore magna aliquam erat volutpat. Ut wisi enim ad minim veniam, quis nostrud exea commodo consequat. Duis</p>
      <p>Lorem ipsum dolor sit amet, consectetuer adipiscing elit, sed diam nonummy nibh euismod tincidunt ut laoreet dolore magna aliquam erat volutpat. Ut wisi enim ad minim veniam, quis nostrud exea commodo consequat. Duis</p>
    </div>
  </section>

  <section class="label label--lime">
    <div class="copy copy--left">
      <h3>INGREDIENTS</h3>
      <p>Lorem ipsum dolor sit amet, consectetuer adipiscing elit, sed diam nonummy nibh euismod tincidunt ut laoreet dolore magna aliquam erat volutpat. Ut wisi enim ad minim veniam, quis nostrud exea commodo consequat. Duis</p>
      <p>Lorem ipsum dolor sit amet, consectetuer adipiscing elit, sed diam nonummy nibh euismod tincidunt ut laoreet dolore magna aliquam erat volutpat. Ut wisi enim ad minim</p>
      <p>Lorem ipsum dolor sit amet, consectetuer adipiscing elit, sed diam nonummy nibh euismod tincidunt ut laoreet dolore magna aliquam erat volutpat. Ut wisi enim ad minim veniam, quis nostrud exea commodo consequat. Duis</p>
    </div>
    <div class="fruit-art" role="img" aria-label="Whole and halved limes with leaves inside a splash of water"></div>
    <div class="brand-name"><span class="brand-dot"></span>kestrola</div>
    <div class="product-name">KOLTA</div>
    <div class="flavor-name">Mojito</div>
    <div class="copy copy--right">
      <p>Lorem ipsum dolor sit amet, consectetuer adipiscing elit, sed diam nonummy nibh euismod tincidunt ut laoreet dolore magna aliquam erat volutpat. Ut wisi enim ad minim veniam, quis nostrud exea commodo consequat. Duis</p>
      <p>Lorem ipsum dolor sit amet, consectetuer adipiscing elit, sed diam nonummy nibh euismod tincidunt ut laoreet dolore magna aliquam erat volutpat. Ut wisi enim ad minim veniam, quis nostrud exea commodo consequat. Duis</p>
      <p>Lorem ipsum dolor sit amet, consectetuer adipiscing elit, sed diam nonummy nibh euismod tincidunt ut laoreet dolore magna aliquam erat volutpat. Ut wisi enim ad minim veniam, quis nostrud exea commodo consequat. Duis</p>
    </div>
  </section>

  <p class="caption">The label is created using dummy text on both sides. If you are interested in this design, provide<br>the other details required for the design as shown here.</p>
</div>
</body>
</html>
```